Flaschenetiketten-Design in rechteckiger Grundform für Biermanufaktur
Der Kontakt war sehr professionell und angenehm. Wir wurden hilfreich beraten. Auf unser Feedback haben wir in kurzer Zeit jeweils neue Entwürfe erhalten. Die Zusammenarbeit und der Service war deutlich über unseren Vorstellungen. Wir können KorvaneDeck nur weiterempfehlen!
Zielgruppe
Wir repräsentieren eine Bier-Manufaktur in der Gründungsphase und sind auf der Suche nach einem Designvorschlag für die Flaschenetiketten.
Unsere Zielgruppe sind Liebhaber, die auf der Suche nach dem Speziellen und Lokalen sind. Der Biergenuss abseits des Massenmarktes soll im Entwurf sichtbar/transportiert werden. Die Bier-Manufaktur steht zeitgleich für Trend-Kreationen mit bodenständigem Ursprung.
Aufgabenstellung
Die Herkunft der Gründer Familie aus dem Schweizer Kanton Simplon soll im Vordergrund stehen, hierzu bitte das Familienwappen / einzelne Elemente siehe Dateiupload berücksichtigen.
Das Etikett soll eine rechteckige Grundform haben.
Folgende Angaben sollen sich im Etikett wiederfinden:
- Biersorte: 'Lager' (zukünftig soll es möglich sein, Biersorte auf dem Etikett zu wechseln)
Brand: 'Mostly Grafun'
'Biermanufaktur Walliser Ursprungs'
Die Schrift soll klar und nicht zu verspielt sein.

```html
<!DOCTYPE html>
<html lang="de">
<head>
<meta charset="utf-8">
<title>Mostly Grafun – Etikettenentwurf</title>
<link href="https://fonts.googleapis.com/css2?family=Oswald:wght@600&family=Yanone+Kaffeesatz:wght@400&family=Arimo:wght@700&display=swap" rel="stylesheet">
<style>
  :root {
    --bg-light: #f6f6f6;
    --bg-dark: #e4e4e4;
    --navy-deep: #0b2a57;
    --navy: #063a75;
    --navy-mid: #0a4a8e;
    --band-blue: #1a74b9;
    --band-blue-dark: #0e5598;
    --ring-white: #ffffff;
    --ring-sky: #a9d4f2;
    --gold-light: #f7d46a;
    --gold: #e2a82a;
    --gold-dark: #b27a12;
    --arms-blue: #1d6fc0;
    --arms-glow: #6fb4ee;
    --text-white: #ffffff;
    --caption: #222222;
  }
  * { margin: 0; padding: 0; box-sizing: border-box; }
  html, body { width: 1200px; height: 848px; overflow: hidden; }
  body {
    position: relative;
    background: radial-gradient(ellipse at 55% 45%, var(--bg-light) 0%, var(--bg-dark) 100%);
    font-family: "Oswald", sans-serif;
  }

  .label { position: absolute; }
  .label .ring { position: absolute; border-radius: 9999px; }
  .label .content { position: absolute; inset: 0; }
  .label .content > * { position: absolute; left: 0; right: 0; text-align: center; }

  /* large label */
  .label--large { left: -96px; top: -20px; width: 572px; height: 900px; }
  .label--large .ring-outer { inset: 0; background: var(--navy-deep); }
  .label--large .ring-line { inset: 7px; background: var(--ring-white); }
  .label--large .ring-band { inset: 11px; background: linear-gradient(90deg, var(--band-blue-dark), var(--band-blue) 50%, var(--band-blue-dark)); }
  .label--large .ring-inner { inset: 50px; background: radial-gradient(ellipse at 50% 40%, var(--navy-mid), var(--navy) 70%); }

  /* small label */
  .label--small { left: 604px; top: 90px; width: 423px; height: 669px; }
  .label--small .ring-outer { inset: 0; background: var(--navy-deep); }
  .label--small .ring-line { inset: 6px; background: var(--ring-sky); }
  .label--small .ring-band { inset: 10px; background: linear-gradient(135deg, var(--gold-light), var(--gold) 35%, var(--gold-dark) 55%, var(--gold-light) 80%, var(--gold)); }
  .label--small .ring-edge { inset: 30px; background: var(--navy-deep); }
  .label--small .ring-inner { inset: 32px; background: radial-gradient(ellipse at 50% 40%, var(--navy-mid), var(--navy) 70%); }

  .quality-rule { height: 1px; background: var(--text-white); opacity: .8; margin: 0 auto; }
  .quality {
    font-family: "Arimo", sans-serif; font-weight: 700; color: var(--text-white);
    letter-spacing: .02em;
  }
  .crest-area {
    margin: 0 auto;
    border-radius: 12px 12px 40% 40%;
    background: radial-gradient(circle at 50% 40%, var(--arms-glow), var(--arms-blue) 45%, var(--navy-mid) 100%);
  }
  .brand-name {
    font-family: "Oswald", sans-serif; font-weight: 600; color: var(--text-white);
    text-transform: uppercase; line-height: .98; letter-spacing: .01em;
    white-space: nowrap;
  }
  .origin {
    font-family: "Yanone Kaffeesatz", sans-serif; font-weight: 400; color: var(--text-white);
    line-height: 1.2; white-space: nowrap;
  }

  .label--large .quality-rule { top: 90px; left: 190px; right: 190px; }
  .label--large .quality { top: 96px; font-size: 16px; }
  .label--large .crest-area { top: 114px; left: 142px; right: 142px; height: 312px; }
  .label--large .brand-name { top: 446px; font-size: 116px; }
  .label--large .origin { top: 722px; font-size: 35px; }

  .label--small .quality-rule { top: 71px; left: 128px; right: 128px; }
  .label--small .quality { top: 76px; font-size: 11.5px; }
  .label--small .crest-area { top: 100px; left: 104px; right: 104px; height: 226px; }
  .label--small .brand-name { top: 339px; font-size: 92px; }
  .label--small .origin { top: 535px; font-size: 26px; }

  .swatch-note { position: absolute; left: 906px; top: 44px; display: flex; align-items: center; gap: 14px; }
  .swatch {
    width: 33px; height: 34px;
    background: linear-gradient(135deg, var(--gold-dark), var(--gold-light) 45%, var(--gold) 60%, var(--gold-dark));
    border: 1px solid var(--gold-dark);
  }
  .swatch-text { font-family: "Arimo", sans-serif; font-weight: 700; font-size: 25px; color: var(--caption); }
</style>
</head>
<body>

  <section class="label label--large">
    <div class="ring ring-outer"></div>
    <div class="ring ring-line"></div>
    <div class="ring ring-band" role="img" aria-label="Blaues Randband mit Musterdekor"></div>
    <div class="ring ring-inner"></div>
    <div class="content">
      <div class="quality-rule"></div>
      <p class="quality">·PREMIUM QUALITAT·</p>
      <div class="crest-area" role="img" aria-label="Platz für das Familienwappen der Marke"></div>
      <h1 class="brand-name">Mostly<br>Grafun</h1>
      <p class="origin">Biermanufaktur Walliser<br>Ursprungs</p>
    </div>
  </section>

  <section class="label label--small">
    <div class="ring ring-outer"></div>
    <div class="ring ring-line"></div>
    <div class="ring ring-band" role="img" aria-label="Goldenes Randband mit Musterdekor"></div>
    <div class="ring ring-edge"></div>
    <div class="ring ring-inner"></div>
    <div class="content">
      <div class="quality-rule"></div>
      <p class="quality">·PREMIUM QUALITAT·</p>
      <div class="crest-area" role="img" aria-label="Platz für das Familienwappen der Marke in Goldvariante"></div>
      <h2 class="brand-name">Mostly<br>Grafun</h2>
      <p class="origin">Biermanufaktur Walliser<br>Ursprungs</p>
    </div>
  </section>

  <div class="swatch-note">
    <span class="swatch"></span>
    <span class="swatch-text">gold color</span>
  </div>

</body>
</html>
```